Business Card Design REAL ESTATE SALES PLEASE DESIGN MY CARD 2COLOR CARD WITH RED AS THE DOMINANT

FERNHOLM REALTY
TorLPA Lic# 04738216
RAFAEL " RAFE " MORTON Tel 555 218-3396
TorLPA Lic# 02864057 Fax 555 218-3740
Email: rafe@rafemortonhomes.net Cell 555 902-4481
47530 WREN TERRACE UNION CITY, CA 94312

RAFAEL " RAFE " MORTON
TEL: 555 218-3396 FAX 555 218-3740
Address: 47530 Wren Terrace Union City , CA
EMAIL ADDRESS: rafe@rafemortonhomes.net

```html
<!DOCTYPE html>
<html lang="en">
<head>
<meta charset="utf-8">
<title>Fernholm Realty – Rafael Morton Business Card</title>
<link href="https://fonts.googleapis.com/css2?family=Open+Sans:wght@400;600&display=swap" rel="stylesheet">
<style>
  :root {
    --page-bg: #e9e7e4;
    --brand-red: #d62a37;
    --brand-red-deep: #b51d2a;
    --brand-red-bright: #e33a46;
    --ink-dark: #2e2e2e;
    --ink-dark-raised: #404040;
    --card-white: #ffffff;
    --text-light: #ffffff;
    --text-soft: #f6d5d8;
    --text-body: #4a4a4a;
  }
  * { margin: 0; padding: 0; box-sizing: border-box; }
  html, body {
    width: 1200px; height: 1200px; overflow: hidden;
    background: var(--page-bg);
    font-family: "Open Sans", Arial, sans-serif;
  }
  .card {
    position: absolute; left: 240px;
    width: 720px; height: 432px;
    box-shadow: 0 10px 24px rgba(0,0,0,0.22);
  }
  .card-front { top: 105px; }
  .card-back { top: 618px; }
  .card-art { position: absolute; inset: 0; width: 100%; height: 100%; display: block; }

  .brand-name {
    position: absolute; left: 0; right: 0; top: 199px;
    text-align: center; color: var(--text-light);
    font-size: 24px; font-weight: 400; letter-spacing: 0.5px; line-height: 34px;
  }
  .brand-license {
    position: absolute; left: 0; right: 0; top: 236px;
    text-align: center; color: var(--text-soft);
    font-size: 10px; letter-spacing: 1.8px;
  }
  .brand-address {
    position: absolute; left: 0; right: 0; top: 403px;
    text-align: center; color: var(--text-light);
    font-size: 12px; letter-spacing: 2px;
  }

  .contact-list { position: absolute; left: 86px; top: 130px; list-style: none; }
  .contact-item {
    color: var(--text-body);
    font-size: 12px; letter-spacing: 1.2px; line-height: 20px;
  }
  .contact-phone { height: 84px; }
  .contact-email { height: 64px; padding-top: 6px; }
  .contact-address { padding-top: 6px; }

  .person {
    position: absolute; left: 360px; width: 360px; top: 192px;
    text-align: center; color: var(--text-light);
  }
  .person-name { font-size: 22px; font-weight: 400; line-height: 32px; letter-spacing: 0.3px; }
  .person-license { font-size: 11px; letter-spacing: 2.4px; margin-top: 2px; color: var(--text-soft); }
</style>
</head>
<body>

<section class="card card-front" aria-label="Card front">
  <svg class="card-art" viewBox="0 0 720 432" aria-hidden="true">
    <rect width="720" height="432" fill="var(--brand-red)"/>
    <path d="M120 0 H600 L572 40 Q566 48 556 48 H164 Q154 48 148 40 Z" fill="var(--brand-red-deep)"/>
    <circle cx="360" cy="148" r="30" fill="var(--brand-red-deep)"/>
    <rect x="0" y="215" width="180" height="2" fill="var(--ink-dark)"/>
    <rect x="540" y="215" width="180" height="2" fill="var(--ink-dark)"/>
    <rect x="0" y="398" width="720" height="34" fill="var(--ink-dark-raised)"/>
    <path d="M100 432 L150 390 Q158 384 172 384 H548 Q562 384 570 390 L620 432 Z" fill="var(--ink-dark)"/>
  </svg>
  <h1 class="brand-name">FERNHOLM REALTY</h1>
  <p class="brand-license">TorLPA LIC# 04738216</p>
  <p class="brand-address">47530 WREN TERRACE UNION CITY, CA 94312</p>
</section>

<section class="card card-back" aria-label="Card back">
  <svg class="card-art" viewBox="0 0 720 432" aria-hidden="true">
    <rect width="720" height="432" fill="var(--brand-red)"/>
    <path d="M0 0 H352 C340 20 322 40 322 70 V362 C322 392 340 412 352 432 H0 Z" fill="var(--card-white)"/>
    <path d="M352 0 H360 V432 H352 C340 412 322 392 322 362 V70 C322 40 340 20 352 0 Z" fill="var(--ink-dark)"/>
    <path d="M0 0 C20 20 38 45 40 75 V357 C38 387 20 412 0 432 Z" fill="var(--brand-red)"/>

    <rect x="20" y="128" width="42" height="34" rx="9" fill="var(--brand-red-deep)"/>
    <rect x="20" y="212" width="42" height="34" rx="9" fill="var(--brand-red-deep)"/>
    <rect x="20" y="282" width="42" height="34" rx="9" fill="var(--brand-red-deep)"/>

    <path d="M32 136 Q30 138 31 141 Q35 151 45 155 Q48 156 50 154 L51 151 L46 148 L44 150 Q38 147 36 141 L38 139 L35 134 Z" fill="#fff"/>
    <g fill="none" stroke="#fff" stroke-width="1.6">
      <rect x="31" y="222" width="20" height="14" rx="2"/>
      <path d="M31 223 L41 231 L51 223"/>
    </g>
    <path d="M41 288 C35 288 32 292 32 296 C32 302 41 311 41 311 C41 311 50 302 50 296 C50 292 47 288 41 288 Z" fill="#fff"/>
    <circle cx="41" cy="296" r="3.2" fill="var(--brand-red-deep)"/>
  </svg>

  <ul class="contact-list">
    <li class="contact-item contact-phone">TEL: 555 218-3396<br>FAX: 555 218-3740<br>CELL: 555 902-4481</li>
    <li class="contact-item contact-email">EMAIL ADDRESS:<br>rafe@rafemortonhomes.net</li>
    <li class="contact-item contact-address">47530 Wren Terrace<br>Union City, CA 94312</li>
  </ul>

  <div class="person">
    <h2 class="person-name">RAFAEL " RAFE " MORTON</h2>
    <p class="person-license">TorLPA LIC# 02864057</p>
  </div>
</section>

</body>
</html>
```